TovarTunes poster

We need a poster to promote my live music show for hotels, Im playing for tourists in hotels in Palma de Mallorca, Spain, I would like to see the url of my web site in the poster www.tovartunes.es, in the web site you can see some of my music, thx

```html
<!DOCTYPE html>
<html lang="en">
<head>
<meta charset="utf-8">
<title>TovarTunes – Live Music Poster</title>
<link href="https://fonts.googleapis.com/css2?family=Marcellus&display=swap" rel="stylesheet">
<style>
  :root{
    --paper:#ffffff;
    --panel-top:#c6a674;
    --panel-mid:#e2cc9f;
    --panel-bottom:#f6ebcf;
    --ink:#2a2318;
    --brown:#7b6244;
    --band:#7d6a4b;
    --band-text:#ffffff;
    --curl-light:#f4e3b8;
    --curl-dark:#a9874f;
    --ornament:#b89a68;
  }
  html,body{margin:0;padding:0;overflow:hidden;background:var(--paper);}
  .poster{
    position:relative;width:849px;height:1200px;overflow:hidden;
    background:var(--paper);box-sizing:border-box;border:1px solid #9a9a9a;
    font-family:"Marcellus",serif;color:var(--brown);
  }
  .panel{
    position:absolute;left:29px;top:39px;width:791px;height:1121px;
    background:linear-gradient(180deg,var(--panel-top) 0%,var(--panel-mid) 45%,var(--panel-bottom) 100%);
    border:1px solid #b59a6c;box-sizing:border-box;
  }
  .brand{
    position:absolute;left:0;right:0;top:92px;text-align:center;
    color:var(--ink);line-height:1;
  }
  .brand-name{display:block;font-size:66px;letter-spacing:2px;}
  .brand-tagline{display:block;font-size:26px;letter-spacing:5px;margin-top:8px;}
  .staff-ornament{
    position:absolute;left:336px;top:212px;width:180px;height:70px;border-radius:8px;
    background:linear-gradient(180deg,rgba(123,98,68,.22),rgba(123,98,68,.12));
  }
  .window{position:absolute;left:0;top:0;}
  .event{
    position:absolute;left:0;right:0;top:998px;display:flex;justify-content:center;align-items:center;
  }
  .save{font-size:27px;line-height:1;text-align:center;padding-right:10px;border-right:1px solid var(--brown);}
  .save small{display:block;font-size:18px;margin-top:6px;}
  .date{font-size:30px;line-height:1.08;padding-left:10px;}
  .year{font-size:27px;writing-mode:vertical-rl;transform:rotate(180deg);margin:0 6px;line-height:1;}
  .time{font-size:26px;line-height:1.25;}
  .address{
    position:absolute;left:226px;width:398px;top:1073px;height:22px;
    border-top:1px solid var(--brown);border-bottom:1px solid var(--brown);
    font-size:15px;display:flex;align-items:center;justify-content:center;gap:4px;
  }
  .contact-band{
    position:absolute;left:29px;top:1116px;width:791px;height:44px;background:var(--band);
    display:flex;align-items:center;justify-content:center;gap:26px;color:var(--band-text);font-size:22px;
  }
  .contact-item{display:flex;align-items:center;gap:7px;}
  .contact-item svg{width:20px;height:20px;}
</style>
</head>
<body>
<div class="poster">
  <div class="panel"></div>

  <div class="brand">
    <span class="brand-name">Tovar</span>
    <span class="brand-tagline">TUNES</span>
  </div>
  <div class="staff-ornament" role="img" aria-label="Music staff with treble clef and notes ornament"></div>

  <svg class="window" width="849" height="1200" viewBox="0 0 849 1200">
    <defs>
      <linearGradient id="scene" x1="0" y1="0" x2="0" y2="1">
        <stop offset="0" stop-color="#a9c0d6"/>
        <stop offset=".3" stop-color="#6f7f6c"/>
        <stop offset=".5" stop-color="#4f6f8c"/>
        <stop offset=".72" stop-color="#3b3f44"/>
        <stop offset="1" stop-color="#b9b3ab"/>
      </linearGradient>
      <linearGradient id="curl" x1="0" y1="0" x2="1" y2="1">
        <stop offset="0" stop-color="var(--curl-light)"/>
        <stop offset=".55" stop-color="#d6b97f"/>
        <stop offset="1" stop-color="var(--curl-dark)"/>
      </linearGradient>
    </defs>
    <polygon points="424,312 759,642 424,968 90,642" fill="url(#scene)" role="img"
      aria-label="Photo of a guitarist performing live, seated on a seaside hotel terrace at dusk"/>
    <g fill="none" stroke="url(#curl)" stroke-width="30" stroke-linejoin="round">
      <path d="M424,312 L759,642"/>
      <path d="M759,642 L424,968"/>
      <path d="M424,968 L90,642"/>
      <path d="M90,642 L424,312"/>
    </g>
    <g fill="none" stroke="rgba(90,65,30,.35)" stroke-width="2">
      <polygon points="424,334 736,642 424,946 113,642"/>
    </g>
  </svg>

  <div class="event">
    <div class="save">SAVE<small>THE DATE</small></div>
    <div class="date">SUNDAY<br>2nd JULY</div>
    <div class="year">2019</div>
    <div class="time">5pm to<br>10pm</div>
  </div>

  <div class="address">
    <svg width="12" height="14" viewBox="0 0 12 14" aria-hidden="true"><path d="M6 1a4 4 0 0 0-4 4c0 3 4 8 4 8s4-5 4-8a4 4 0 0 0-4-4z" fill="none" stroke="currentColor"/><circle cx="6" cy="5" r="1.4" fill="none" stroke="currentColor"/></svg>
    #2190, Harbor Lane Park Next Marina Tower
  </div>

  <div class="contact-band">
    <span class="contact-item">
      <svg viewBox="0 0 20 20" aria-hidden="true"><g fill="none" stroke="#fff" stroke-width="1.3"><circle cx="10" cy="10" r="8"/><ellipse cx="10" cy="10" rx="3.5" ry="8"/><path d="M2 10h16M3.5 6h13M3.5 14h13"/></g></svg>
      www.tovartunes.es
    </span>
    <span class="contact-item">
      <svg viewBox="0 0 20 20" aria-hidden="true"><g fill="none" stroke="#fff" stroke-width="1.3"><rect x="2" y="4" width="16" height="12"/><path d="M2 4l8 7 8-7"/></g></svg>
      songs@tovartunes.es
    </span>
    <span class="contact-item">
      <svg viewBox="0 0 20 20" aria-hidden="true"><g fill="none" stroke="#fff" stroke-width="1.3"><path d="M2 8c0-3 4-4 8-4s8 1 8 4l-3 1-1-2H6L5 9z"/><rect x="4" y="10" width="12" height="6" rx="1"/><circle cx="10" cy="13" r="1.5"/></g></svg>
      5550192834
    </span>
  </div>
</div>
</body>
</html>
```